BOLD & MINIMALIST DESIGN NEEDED

We want a very bold but minimalistic business card design that is impactful and utilizes both sides of the business card. Our current logo is included for your use.

We want bold fonts and good use of negative space. We don't want the logo to overpower the design.

Target Market(s)

Professionals who are building new commercial buildings.

Industry/Entity Type

Construction

Contact Information for Business Card

Name, Title, email, office phone, cell phone, website

Font styles to use
Serif
Sans Serif

Requirements
Must have
• Bold design!

```html
<!DOCTYPE html>
<html lang="en">
<head>
<meta charset="utf-8">
<title>Ridgeline Build Co. — Stationery Set</title>
<link rel="stylesheet" href="https://fonts.googleapis.com/css2?family=Montserrat:wght@400;500;700;800&family=Open+Sans:wght@400&display=swap">
<style>
:root{
  --board:#3a3d3f;
  --label:#ffffff;
  --paper:#ffffff;
  --ink:#050808;
  --green:#6cc04a;
  --rule:#cfcfcf;
  --muted:#8a8a8a;
}
*{box-sizing:border-box;margin:0;padding:0}
html,body{width:953px;height:1200px;overflow:hidden}
body{background:var(--board);position:relative;font-family:"Montserrat",sans-serif;color:var(--ink)}
.label{position:absolute;font-family:"Open Sans",sans-serif;font-size:17px;color:var(--label);line-height:1}
.piece{position:absolute;background:var(--paper);overflow:hidden}
.wordmark{position:absolute;left:0;right:0;text-align:center;font-weight:800;letter-spacing:.5px;color:var(--ink);white-space:nowrap}
.wordmark .dot{display:inline-block;width:.55em;height:.55em;background:var(--green);margin-right:.35em;vertical-align:.08em}
.curve{position:absolute;left:0;bottom:0;width:100%}
.contact{position:absolute;left:0;right:0;text-align:center;color:#fff;font-size:7.5px;line-height:1.5;white-space:nowrap}
.contact .ico{display:inline-block;width:5px;height:6px;background:var(--green);margin-right:3px;vertical-align:-.5px;border-radius:1px}
.contact .sep{margin:0 4px}
.contact .addr{display:inline-block;border-top:.5px solid #555;margin-top:2px;padding-top:2px;letter-spacing:.6px}

/* business card */
.card{width:300px;height:171px;border-radius:2px}
.card-back{left:120px;top:130px;background:radial-gradient(ellipse at 50% 40%,#2a2a2a,#050505 70%)}
.card-back .wordmark{top:68px;font-size:16px;color:#fff}
.card-back .web{position:absolute;left:0;right:0;top:96px;text-align:center;color:var(--green);font-size:7.5px;letter-spacing:3px}
.card-front{left:120px;top:318px}
.card-front .wordmark{top:22px;font-size:14px}
.card-front .person{position:absolute;left:0;right:0;top:52px;text-align:center;font-weight:700;font-size:10px}
.card-front .role{position:absolute;left:0;right:0;top:66px;text-align:center;font-size:7px;color:var(--muted)}

/* letterhead */
.letterhead{left:499px;top:97px;width:377px;height:488px}
.letterhead .wordmark{top:56px;font-size:17px}

/* note pad */
.notepad{left:77px;top:619px;width:361px;height:253px}
.notepad .wordmark{top:40px;font-size:13px}
.notepad .lines{position:absolute;left:12px;right:14px;top:73px}
.notepad .lines span{display:block;height:16.5px;border-top:1px solid var(--rule)}

/* compliment slip */
.compslip{left:492px;top:691px;width:384px;height:181px}
.compslip .wordmark{top:50px;font-size:14px}
.compslip .greeting{position:absolute;left:0;right:0;top:87px;text-align:center;color:var(--green);font-weight:700;font-size:12px;letter-spacing:1.5px}

/* envelopes */
.env{width:387px;height:167px;top:952px}
.env-front{left:77px}
.env-front .wordmark{left:10px;right:auto;top:38px;font-size:11px;text-align:left}
.env-front .return{position:absolute;left:14px;top:64px;width:82px;border-top:1px solid var(--green);padding-top:4px;text-align:center;font-size:6.5px;line-height:1.35}
.env-back{left:498px}
.env-back .flap{position:absolute;left:0;top:0;width:100%;height:64px}
.env-back .wordmark{top:37px;font-size:10px;color:#fff}
</style>
</head>
<body>

<div class="label" style="left:77px;top:63px">Business card_5</div>
<div class="label" style="left:498px;top:63px">Letterhead_5</div>
<div class="label" style="left:77px;top:586px">Note Pads_5</div>
<div class="label" style="left:492px;top:656px">Comp Slips_5</div>
<div class="label" style="left:77px;top:916px">ENV Front_5</div>
<div class="label" style="left:498px;top:916px">ENV Back_5</div>

<section class="piece card card-back">
  <div class="wordmark"><span class="dot"></span>RIDGELINE BUILD CO.</div>
  <div class="web">www.ridgeline-bc.com</div>
</section>

<section class="piece card card-front">
  <div class="wordmark"><span class="dot"></span>RIDGELINE BUILD CO.</div>
  <div class="person">Daniel Foster</div>
  <div class="role">Founder</div>
  <svg class="curve" height="78" viewBox="0 0 300 78" preserveAspectRatio="none">
    <path d="M0 40 Q150 -6 300 40 L300 78 L0 78Z" fill="#050808"/>
  </svg>
  <div class="contact" style="top:110px">
    <span class="ico"></span>555-013-9000<span class="sep">|</span><span class="ico"></span>555-014-2200<br>
    <span class="ico"></span>info@ridgeline-bc.com<span class="sep">|</span><span class="ico"></span>www.ridgeline-bc.com<br>
    <span class="addr">1420 Cedar Hollow Rd. Pine Ridge, GA 30500</span>
  </div>
</section>

<section class="piece letterhead">
  <div class="wordmark"><span class="dot"></span>RIDGELINE BUILD CO.</div>
  <svg class="curve" height="70" viewBox="0 0 377 70" preserveAspectRatio="none">
    <path d="M0 38 Q188 -16 377 38 L377 70 L0 70Z" fill="#050808"/>
    <path d="M0 36.5 Q188 -17.5 377 36.5" fill="none" stroke="#6cc04a" stroke-width="1.2"/>
  </svg>
  <div class="contact" style="top:438px">
    <span class="ico"></span>555-013-9000<span class="sep">|</span><span class="ico"></span>555-014-2200<br>
    <span class="ico"></span>info@ridgeline-bc.com<span class="sep">|</span><span class="ico"></span>www.ridgeline-bc.com<br>
    <span class="addr">1420 Cedar Hollow Rd. Pine Ridge, GA 30500</span>
  </div>
</section>

<section class="piece notepad">
  <div class="wordmark"><span class="dot"></span>RIDGELINE BUILD CO.</div>
  <div class="lines"><span></span><span></span><span></span><span></span><span></span><span></span><span></span><span></span></div>
  <svg class="curve" height="66" viewBox="0 0 361 66" preserveAspectRatio="none">
    <path d="M0 36 Q180 -14 361 36 L361 66 L0 66Z" fill="#050808"/>
    <path d="M0 34.5 Q180 -15.5 361 34.5" fill="none" stroke="#6cc04a" stroke-width="1.2"/>
  </svg>
  <div class="contact" style="top:202px">
    <span class="ico"></span>555-013-9000<span class="sep">|</span><span class="ico"></span>555-014-2200<br>
    <span class="ico"></span>info@ridgeline-bc.com<span class="sep">|</span><span class="ico"></span>www.ridgeline-bc.com<br>
    <span class="addr">1420 Cedar Hollow Rd. Pine Ridge, GA 30500</span>
  </div>
</section>

<section class="piece compslip">
  <div class="wordmark"><span class="dot"></span>RIDGELINE BUILD CO.</div>
  <div class="greeting">With Compliments</div>
  <svg class="curve" height="84" viewBox="0 0 384 84" preserveAspectRatio="none">
    <path d="M0 44 Q192 -12 384 44 L384 84 L0 84Z" fill="#050808"/>
    <path d="M0 42.5 Q192 -13.5 384 42.5" fill="none" stroke="#6cc04a" stroke-width="1.2"/>
  </svg>
  <div class="contact" style="top:123px">
    <span class="ico"></span>555-013-9000<span class="sep">|</span><span class="ico"></span>555-014-2200<br>
    <span class="ico"></span>info@ridgeline-bc.com<span class="sep">|</span><span class="ico"></span>www.ridgeline-bc.com<br>
    <span class="addr">1420 Cedar Hollow Rd. Pine Ridge, GA 30500</span>
  </div>
</section>

<section class="piece env env-front">
  <div class="wordmark"><span class="dot"></span>RIDGELINE</div>
  <div class="return">1420 Cedar Hollow Rd.<br>Pine Ridge, GA 30500</div>
</section>

<section class="piece env env-back">
  <svg class="flap" viewBox="0 0 387 64" preserveAspectRatio="none">
    <path d="M0 0 L387 0 C376 22 370 32 345 36 L212 58 Q193 63 175 58 L42 36 C17 32 11 22 0 0Z" fill="#050808"/>
  </svg>
  <div class="wordmark">RIDGELINE</div>
</section>

</body>
</html>
```